Construction business card

We are a family run and family oriented business in Philadelphia and we are starting new. We proudly serve the public by giving our customers great work at affordable prices. We can do all aspects of construction from the roof to the basement. We would like our business card to incorporate tools and family.
Updates

Can y'all please incorporate a bulldog

Industry/Entity Type

Construction

Contact Information for Business Card

Harwick Builders LLC, Dennis Oakley, 7819 W Lindel st Philadelphia Pa 19188, CEO Main phone (215) 555-0193 cellphone 215-555-0147 Dennis oakley Jr cellphone 267-555-0162 email harwickbuildersllc@mailtrove.example

Colors
f78f20
ffffff
1b1b1b

```html
<!DOCTYPE html>
<html lang="en">
<head>
<meta charset="utf-8">
<title>Harwick Builders LLC – Business Card</title>
<link rel="stylesheet" href="https://fonts.googleapis.com/css2?family=Open+Sans:wght@400;600;700&display=swap">
<style>
  :root {
    --orange: #f78f20;
    --orange-light: #f9a543;
    --white: #ffffff;
    --ink: #1b1b1b;
    --backdrop: #e6e4e1;
  }
  * { margin: 0; padding: 0; box-sizing: border-box; }
  html, body {
    width: 1200px;
    height: 800px;
    overflow: hidden;
    background: var(--backdrop);
    font-family: "Open Sans", sans-serif;
    color: var(--ink);
  }
  .sheet {
    width: 1200px;
    height: 800px;
    display: flex;
    align-items: center;
    justify-content: center;
    gap: 60px;
  }
  .card {
    position: relative;
    width: 520px;
    height: 297px;
    background: var(--white);
    overflow: hidden;
    box-shadow: 0 6px 18px rgba(0,0,0,0.18);
  }
  .card__band {
    position: absolute;
    inset: 0;
    width: 100%;
    height: 100%;
  }

  /* Front */
  .brand {
    position: absolute;
    top: 70px;
    left: 0;
    right: 0;
    text-align: center;
    font-weight: 700;
    font-size: 36px;
    letter-spacing: 0.5px;
    color: var(--ink);
  }
  .holder {
    position: absolute;
    left: 0;
    right: 0;
    bottom: 34px;
    text-align: center;
    font-size: 30px;
    font-weight: 700;
    color: var(--ink);
  }
  .holder__title {
    font-weight: 400;
    font-size: 22px;
  }

  /* Back */
  .contacts {
    position: absolute;
    top: 34px;
    right: 40px;
    text-align: right;
    font-size: 14px;
    line-height: 1.45;
  }
  .contacts__label { color: var(--orange); font-weight: 400; }
  .contacts__value { color: var(--ink); font-weight: 600; }
  .contacts__person {
    margin-top: 12px;
    font-weight: 700;
    font-size: 15px;
  }
  .address {
    position: absolute;
    left: 150px;
    bottom: 58px;
    font-size: 17px;
    font-weight: 600;
    color: var(--ink);
    transform: rotate(-9deg);
    transform-origin: left bottom;
  }
</style>
</head>
<body>
<main class="sheet">

  <section class="card card--front" aria-label="Business card front">
    <svg class="card__band" viewBox="0 0 520 297" preserveAspectRatio="none" aria-hidden="true">
      <defs>
        <linearGradient id="frontBand" x1="0" y1="0" x2="0" y2="1">
          <stop offset="0" stop-color="var(--orange-light)"/>
          <stop offset="1" stop-color="var(--orange)"/>
        </linearGradient>
      </defs>
      <path d="M0,200 C150,160 320,205 520,148 L520,297 L0,297 Z" fill="url(#frontBand)"/>
    </svg>
    <h1 class="brand">Harwick Builders LLC</h1>
    <p class="holder">Dennis Oakley, <span class="holder__title">CEO</span></p>
  </section>

  <section class="card card--back" aria-label="Business card back">
    <svg class="card__band" viewBox="0 0 520 297" preserveAspectRatio="none" aria-hidden="true">
      <path d="M0,297 L0,262 L520,180 L520,297 Z" fill="var(--orange)"/>
    </svg>
    <div class="contacts">
      <p><span class="contacts__label">CEO main phone</span> <span class="contacts__value">(215) 555-0193</span></p>
      <p><span class="contacts__label">cellphone</span> <span class="contacts__value">215-555-0147</span></p>
      <p><span class="contacts__label">email</span> <span class="contacts__value">harwickbuildersllc@mailtrove.example</span></p>
      <p class="contacts__person">Dennis oakley Jr</p>
      <p><span class="contacts__label">cellphone</span> <span class="contacts__value">267-555-0162</span></p>
    </div>
    <p class="address">7819 W Lindel st Philadelphia Pa 19188</p>
  </section>

</main>
</body>
</html>
```